Milo Castell Moving DL Flyer

We need a double sided DL flyer to give to patients to let them know that we are moving location.
On one side we would like it to read:
"We Are Moving!" and "November 2017" and our logo.
On the other side we would like it to read:
"Same Great Staff"
"Same Great Service"
"Bigger, Brighter and Better"
"New Location at 42 Quarry Rd"
with a map below (attached)
The flyer should follow our practice branding. Attached is a copy of our business card as an example of this.

```html
<!DOCTYPE html>
<html lang="en">
<head>
<meta charset="utf-8">
<title>Milo Castell Optometry – Moving Flyer</title>
<link href="https://fonts.googleapis.com/css2?family=Open+Sans:wght@400;600;700&display=swap" rel="stylesheet">
<style>
  :root {
    --plum: #523d58;
    --paper: #ffffff;
    --backdrop: #dcdcdc;
    --edge: #a9a9a9;
    --photo-light: #f1eeee;
    --photo-mid: #c9d3e6;
    --photo-skin: #e7c6b4;
    --map-grey: #bdbdbd;
    --map-accent: #f0a0a0;
  }
  * { box-sizing: border-box; margin: 0; padding: 0; }
  html, body { width: 1200px; height: 848px; overflow: hidden; }
  body {
    background: var(--backdrop);
    font-family: "Open Sans", Arial, sans-serif;
    position: relative;
  }
  .flyer {
    position: absolute;
    top: 127px;
    width: 420px;
    height: 594px;
    background: var(--paper);
    overflow: hidden;
  }
  .flyer--front { left: 150px; }
  .flyer--back { left: 630px; border-top: 10px solid var(--edge); }

  /* Front */
  .brand {
    position: absolute; top: 22px; left: 22px;
    display: flex; align-items: center; gap: 8px;
    color: var(--plum);
  }
  .brand__dot { width: 14px; height: 14px; border-radius: 50%; background: var(--plum); }
  .brand__name { font-size: 15px; font-weight: 600; line-height: 1.1; }
  .headline {
    position: absolute; top: 70px; left: 150px;
    color: var(--plum); font-size: 26px; font-weight: 700;
  }
  .date-tag {
    position: absolute; top: 118px; left: 0;
    background: var(--plum); color: var(--paper);
    padding: 10px 22px 10px 24px; line-height: 1;
  }
  .date-tag__month { display: block; font-size: 19px; font-weight: 600; }
  .date-tag__year { display: block; font-size: 40px; font-weight: 700; margin-top: 4px; }
  .feature-name {
    position: absolute; top: 214px; left: 128px;
    color: var(--plum); font-size: 44px; font-weight: 700; line-height: 1.1;
  }
  .sweep { position: absolute; inset: 0; }
  .photo { position: absolute; }
  .photo--clinician {
    left: 16px; bottom: 44px; width: 170px; height: 200px;
    background: radial-gradient(ellipse at 60% 30%, var(--photo-skin) 0 18%, transparent 40%),
                linear-gradient(180deg, var(--photo-light) 40%, var(--photo-mid));
  }

  /* Back */
  .photo--team {
    top: 20px; left: 60px; width: 320px; height: 140px;
    background: linear-gradient(90deg, var(--photo-light), var(--photo-mid) 30%, var(--photo-light) 55%, var(--photo-mid) 85%, var(--photo-light));
  }
  .promise-band {
    position: absolute; top: 150px; left: 0; right: 0; height: 92px;
    background: var(--plum); color: var(--paper);
    display: flex; flex-direction: column; justify-content: center; align-items: center;
    font-size: 18px; font-weight: 700; line-height: 1.4;
  }
  .new-location {
    position: absolute; top: 256px; left: 0; right: 0; text-align: center;
    color: var(--plum); font-size: 20px; font-weight: 700;
  }
  .photo--map {
    top: 296px; left: 50px; width: 320px; height: 230px;
    background: linear-gradient(135deg, var(--map-grey) 0%, #d2c6c6 50%, var(--map-accent) 100%);
  }
  .footer-rule {
    position: absolute; left: 0; right: 0; bottom: 20px; height: 18px;
    background: var(--plum);
  }
  .footer-rule::before {
    content: ""; position: absolute; left: 0; right: 0; top: -8px; height: 3px;
    background: var(--plum);
  }
</style>
</head>
<body>
  <section class="flyer flyer--front">
    <svg class="sweep" width="420" height="594" viewBox="0 0 420 594" aria-hidden="true">
      <path d="M420 90 L420 594 L260 594 C300 430 350 250 400 90 Z" fill="var(--plum)"/>
      <path d="M378 90 C330 250 280 430 236 594" stroke="var(--plum)" stroke-width="8" fill="none"/>
    </svg>
    <div class="brand">
      <span class="brand__dot"></span>
      <span class="brand__name">Milo Castell<br>Optometry</span>
    </div>
    <h1 class="headline">We Are Moving!</h1>
    <div class="date-tag">
      <span class="date-tag__month">November</span>
      <span class="date-tag__year">2017</span>
    </div>
    <p class="feature-name">Milo<br>Castell</p>
    <div class="photo photo--clinician" role="img" aria-label="Photo of a smiling clinician with stethoscope, arms folded"></div>
  </section>

  <section class="flyer flyer--back">
    <div class="photo photo--team" role="img" aria-label="Photo of the practice team in white coats and blue scrubs"></div>
    <div class="promise-band">
      <p>- Same Great Staff</p>
      <p>- Same Great Service</p>
      <p>- Bigger, Brighter and Better</p>
    </div>
    <h2 class="new-location">New Location at 42 Quarry Rd</h2>
    <div class="photo photo--map" role="img" aria-label="Street map showing the new practice location beside the marketplace, car park and neighbouring clinics"></div>
    <div class="footer-rule"></div>
  </section>
</body>
</html>
```